Premium CBD/Hemp company needs packaging and label design

Verdant Halcyon Labs, a premium CBD/Hemp company based in Scottsdale, Arizona is in need of a packaging and label design. We are launching with our flagship product which will be a 30 count capsule and will come in three functions: Pain Relief, Anxiety Support, and Sleep Support. For the purpose of this contest, please design packaging and label for our Anxiety Support product. Our products are physician formulated and all natural. Our main ingredient is CBD/Hemp and is complemented by specific herbs that synergistically work together to give the customer the most effective and desired result. We would like our branding to have a pharmaceutical look and feel with a focus on trust and transparency. We have uploaded our company logo that is to be used on both the packaging and label. We have also uploaded an executed branding questionnaire that will guide you to exactly what we are seeking to achieve as to the look and feel of our brand. Please feel free to contact us with any questions that you may have. The winner of this contest will have the opportunity to work with us on future projects as we will need packaging and label design for our entire Verdant Halcyon Labs product line.

Target Market(s)

See attached branding questionnaire

Industry/Entity Type

Health And Wellness

Font styles to use
Sans Serif

Colors

Designer to choose colors to be used in the design.

Requirements
Must have
• See attached branding questionnaire; Please superimpose labels onto a cobalt blue capsule bottle (see attached)
• >>UPON REVIEW of the FIRST 8 designs, we really like the silver, mildly metallic label background in DESIGN # 21300528, we do not want metalic lettering as that would not look very "Pharmaceutical"
• >>We are in search of a look that is a bit more "Pharmaceutical" than a look that would be more commonly found in a Supplement Store
Nice to have
• "See attached branding questionnaire
Should not have
• See attached branding questionnaire; NO marijuana or cannabis plant on the packaging or label

```html
<!DOCTYPE html>
<html lang="en">
<head>
<meta charset="utf-8">
<title>Verdant Halcyon Labs – Anxiety Support Label</title>
<link rel="stylesheet" href="https://fonts.googleapis.com/css2?family=Barlow:wght@500;600&family=Montserrat:wght@600;800&display=swap">
<style>
  :root {
    --cobalt: #23349a;
    --cobalt-deep: #1b2a85;
    --ink: #1f2a6b;
    --graphite: #474a50;
    --silver-light: #f7f8fa;
    --silver-mid: #e3e5ea;
    --silver-dark: #c9ccd3;
    --page: #ffffff;
    --white: #ffffff;
  }
  html, body {
    margin: 0;
    width: 1200px;
    height: 1200px;
    overflow: hidden;
    background: var(--page);
  }
  .canvas {
    position: relative;
    width: 1200px;
    height: 1200px;
  }
  .label-panel {
    position: absolute;
    left: 280px;
    top: 80px;
    width: 640px;
    height: 1040px;
    overflow: hidden;
    background: linear-gradient(115deg, var(--silver-light) 0%, var(--silver-mid) 38%, var(--silver-light) 55%, var(--silver-dark) 100%);
    box-shadow: 0 10px 40px rgba(0,0,0,0.12);
  }
  .bands {
    position: absolute;
    inset: 0;
    width: 640px;
    height: 1040px;
  }
  .brand-tab {
    position: absolute;
    left: 120px;
    top: 46px;
    width: 400px;
    height: 290px;
    background: var(--white);
    border: 3px solid var(--silver-dark);
    border-top: none;
    border-radius: 0 0 44px 44px;
    box-sizing: border-box;
    display: flex;
    flex-direction: column;
    align-items: center;
    justify-content: center;
    gap: 26px;
  }
  .brand-dot {
    width: 120px;
    height: 120px;
    border-radius: 50%;
    border: 6px solid var(--cobalt);
    box-sizing: border-box;
  }
  .brand-name {
    font-family: "Montserrat", sans-serif;
    font-weight: 600;
    font-size: 25px;
    letter-spacing: 0.04em;
    color: var(--cobalt);
    margin: 0;
  }
  .product-title {
    position: absolute;
    left: 0;
    right: 0;
    top: 420px;
    text-align: center;
  }
  .product-title .function {
    display: block;
    font-family: "Montserrat", sans-serif;
    font-weight: 800;
    font-size: 104px;
    line-height: 1;
    letter-spacing: 0.02em;
    color: var(--cobalt);
  }
  .product-title .support {
    display: block;
    margin-top: 14px;
    font-family: "Montserrat", sans-serif;
    font-weight: 800;
    font-size: 46px;
    line-height: 1;
    letter-spacing: 0.62em;
    padding-left: 0.62em;
    color: var(--graphite);
  }
  .tagline {
    display: inline-block;
    margin-top: 22px;
    padding: 6px 16px;
    background: var(--white);
    border-radius: 14px;
    font-family: "Barlow", sans-serif;
    font-weight: 500;
    font-size: 28px;
    letter-spacing: 0.03em;
    color: var(--cobalt);
  }
  .claim-tab {
    position: absolute;
    left: 80px;
    top: 800px;
    width: 400px;
    height: 150px;
    background: var(--white);
    border-radius: 40px 40px 0 0;
    display: flex;
    flex-direction: column;
    align-items: center;
    justify-content: center;
    font-family: "Barlow", sans-serif;
    font-weight: 600;
    font-size: 25px;
    line-height: 1.35;
    letter-spacing: 0.04em;
    color: var(--ink);
    text-align: center;
  }
</style>
</head>
<body>
<main class="canvas">
  <section class="label-panel" aria-label="Anxiety Support label">
    <svg class="bands" viewBox="0 0 640 1040" aria-hidden="true">
      <defs>
        <linearGradient id="cobaltBand" x1="0" y1="0" x2="1" y2="1">
          <stop offset="0" stop-color="#2a3ca6"/>
          <stop offset="1" stop-color="#1b2a85"/>
        </linearGradient>
      </defs>
      <!-- top band -->
      <path d="M0 0 H640 V34 C460 40 220 60 0 78 Z" fill="url(#cobaltBand)"/>
      <path d="M0 78 C220 60 460 40 640 34 V44 C460 50 220 70 0 90 Z" fill="#b9bcc4"/>
      <!-- bottom band -->
      <path d="M0 905 C200 905 420 895 520 870 C580 855 615 830 640 815 V1040 H0 Z" fill="#b9bcc4"/>
      <path d="M0 918 C200 918 420 908 525 882 C585 867 618 842 640 828 V1040 H0 Z" fill="url(#cobaltBand)"/>
    </svg>

    <header class="brand-tab">
      <div class="brand-dot"></div>
      <p class="brand-name">VERDANT HALCYON LABS</p>
    </header>

    <h1 class="product-title">
      <span class="function">ANXIETY</span>
      <span class="support">SUPPORT</span>
      <span class="tagline">CBD INFUSED HERBAL REMEDIES</span>
    </h1>

    <div class="claim-tab">
      <span>100% NATURAL</span>
      <span>PLANT-BASED FORMULAS</span>
    </div>
  </section>
</main>
</body>
</html>
```